Plastic Business Cards

I am looking for a plastic business card that matches the theme of my company.

Attached will be logo and template to Prindlecraft for printing.

On card please include the following information:

Logo
612-437-9158 Call or Text
www.GlintvaleCo.com

Window Cleaning
Gutter Cleaning & Covers
Christmas Lighting

200+ 5 Star Reviews

```html
<!DOCTYPE html>
<html lang="en">
<head>
<meta charset="utf-8">
<title>Glintvale Window Cleaning – Business Card</title>
<link rel="stylesheet" href="https://fonts.googleapis.com/css2?family=Oswald:wght@500;600&family=Arimo:wght@400&display=swap">
<style>
  :root {
    --page-bg: #eceef1;
    --navy: #00224d;
    --brand-navy: #0a2f66;
    --sky: #1591d6;
    --ice: #c9ecfb;
    --lime: #9acb3a;
    --white: #ffffff;
    --star: #ffcc00;
    --frost-a: #f3ecec;
    --frost-b: #e7d9d9;
  }
  * { margin: 0; padding: 0; box-sizing: border-box; }
  html, body {
    width: 1200px; height: 900px; overflow: hidden;
    background: var(--page-bg);
  }
  .card {
    position: absolute; left: 100px; top: 140px;
    width: 1000px; height: 620px;
    background: var(--navy);
    overflow: hidden;
    box-shadow: 0 18px 40px rgba(0,0,0,.18);
  }
  .card__frost {
    position: absolute; left: 0; top: 0; width: 100%; height: 288px;
    background: linear-gradient(180deg, var(--frost-a) 0%, var(--frost-b) 100%);
    border-bottom: 7px solid var(--sky);
  }
  .brand {
    position: absolute; left: 0; top: 150px; width: 100%;
    display: flex; align-items: center; justify-content: center; gap: 22px;
  }
  .brand__dot {
    width: 92px; height: 92px; border-radius: 50%;
    background: var(--sky);
  }
  .brand__name {
    font-family: "Oswald", sans-serif; font-weight: 600;
    font-size: 62px; line-height: 1; letter-spacing: 1px;
    text-transform: uppercase; color: var(--brand-navy);
  }
  .call {
    position: absolute; left: 0; top: 376px; width: 100%;
    text-align: center;
    font-family: "Oswald", sans-serif; font-weight: 500;
    font-size: 54px; line-height: 1; text-transform: uppercase;
    color: var(--ice); letter-spacing: -0.5px;
  }
  .web {
    position: absolute; left: 0; top: 448px; width: 100%;
    text-align: center;
    font-family: "Arimo", sans-serif; font-size: 29px;
    color: var(--lime);
  }
  .services {
    position: absolute; left: 52px; top: 486px;
    list-style: none;
    font-family: "Arimo", sans-serif; font-size: 30px;
    color: var(--white);
  }
  .services li {
    display: flex; align-items: center; gap: 14px;
    height: 37px;
  }
  .services li::before {
    content: ""; width: 28px; height: 28px; border-radius: 50%;
    background: var(--sky);
  }
  .reviews {
    position: absolute; right: 56px; top: 496px;
    text-align: right;
    font-family: "Arimo", sans-serif; font-size: 29px;
    color: var(--white);
  }
  .reviews__stars { display: block; margin-top: 12px; margin-left: auto; }
</style>
</head>
<body>
  <section class="card">
    <div class="card__frost" role="img" aria-label="Frosted clear plastic showing a softly blurred room behind the card"></div>

    <div class="brand">
      <span class="brand__dot"></span>
      <span class="brand__name">Glintvale Window Cleaning</span>
    </div>

    <p class="call">Call or Text 612-437-9158</p>
    <p class="web">www.GlintvaleCo.com</p>

    <ul class="services">
      <li>Window Cleaning</li>
      <li>Gutter Cleaning &amp; Covers</li>
      <li>Christmas Lighting</li>
    </ul>

    <div class="reviews">
      <p>200+ 5 Star Reviews</p>
      <svg class="reviews__stars" width="180" height="36" viewBox="0 0 180 36" aria-label="Five stars">
        <defs>
          <polygon id="star" points="18,1 22.6,12.6 35,13.2 25.4,21.1 28.6,33.2 18,26.3 7.4,33.2 10.6,21.1 1,13.2 13.4,12.6" fill="var(--star)"/>
        </defs>
        <use href="#star" x="0"/>
        <use href="#star" x="36"/>
        <use href="#star" x="72"/>
        <use href="#star" x="108"/>
        <use href="#star" x="144"/>
      </svg>
    </div>
  </section>
</body>
</html>
```